Book Cover needed - Disinformation and fake news

I need a book cover (front, back, spine) for the 1st edition of a book entitled ‘Marea Silenciosa’ (Means – Silent Tide) and subtitled ‘Los ecos que nadie quiso escuchar’ (Means - The echoes nobody wanted to hear) (inverted commas not to be part of the title and subtitle). The author is ‘Tomás Herreruela’. The finished size of the paperback version will be 5.25" x 8". There will be paperback and e-book versions, so 2 covers will need to be provided: one for the e-book version just with the front cover, and the full book cover for the paperback version.
The final number of pages is expected to be in the region of 350-500 pages. Text for the back cover is down below, and at the bottom of the back cover should have space for the ISBN bar code on the right. The books will be published with PQN - Velmora, so should follow their indications for any specification needed.
The topics discussed include disinformation, fake news, psychological operations. Feel free to design the cover based on those. The design should be original and not include any stock images that have been created by someone else or may require obtaining a copyright license to use.
Back Cover Text (spacing should be respected) :
Oficina del consenso, desinformación, “fake news”... en los últimos años nos hemos visto envueltos en una discusión pública rodeados de estos términos sin terminar de entender exactamente qué significan y lo que es peor, sin saber que realmente nos rodean desde que el hombre es hombre.
En esta obra el autor busca acercanos al mundo de la Marea Silenciosa, aquellas operaciones que buscan influir sobre el comportamiento de la población. Sin hacer uso de un lenguaje excesivamente técnico relata como la evolución de la naturaleza de la guerra a los parámetros del siglo XXI promueve un enfoque del conflicto que no supone un uso de la fuerza tradicional. ¿Para qué atacar las instituciones de un país de forma directa, cuando puedes fomentar el conflicto social entre grupos antagónicos y desestabilizar sin realizar un solo disparo?
¿Cómo razona el ser humano? ¿Son nuestras ideas tan nuestras como creemos? ¿Por qué importa tanto el uso preciso del lenguaje a la hora de comunicarnos?, ¿Cómo nos afectan las razones y emociones de los demás? ¿Por qué tendemos a prestar mayor atención a argumentos que encajen con nuestras propias ideas? ¿Cómo nos afecta la conversación en redes sociales?
Armados con el conocimiento que reside en este libro, quizás, seamos menos susceptibles de caer bajo la influencia de grupos con intereses espurios.
General public with an interest on disinformation - fake news

```html
<!DOCTYPE html>
<html lang="es">
<head>
<meta charset="utf-8">
<title>Marea Silenciosa — Cubierta completa</title>
<link rel="stylesheet" href="https://fonts.googleapis.com/css2?family=Montserrat:wght@400;900&family=Gentium+Book+Plus:wght@400&display=swap">
<style>
  :root {
    --ink-white: #ffffff;
    --night: #140504;
    --ember-dark: #2a0b05;
    --ember: #5a1806;
    --flame: #e8761a;
    --flame-hot: #f6a42c;
    --flame-red: #9c2a0b;
  }
  * { margin: 0; padding: 0; box-sizing: border-box; }
  html, body { width: 1200px; height: 834px; overflow: hidden; background: var(--night); }
  .cover {
    position: relative;
    width: 1200px; height: 834px; overflow: hidden;
    background:
      radial-gradient(ellipse 700px 240px at 760px 834px, rgba(150,45,10,.5), transparent 70%),
      linear-gradient(90deg, var(--night) 0%, #1e0805 35%, var(--ember-dark) 55%, #3d1006 75%, var(--ember) 100%);
    color: var(--ink-white);
  }
  .title { font-family: "Montserrat", sans-serif; font-weight: 900; text-transform: uppercase; text-align: center; line-height: .9; }
  .title .line-1, .title .line-2 { display: block; }
  .subtitle { font-family: "Montserrat", sans-serif; font-weight: 400; text-transform: uppercase; text-align: center; }

  /* Back cover */
  .back { position: absolute; left: 0; top: 0; width: 564px; height: 834px; }
  .back .title { position: absolute; left: 0; width: 548px; top: 50px; }
  .back .title .line-1 { font-size: 70px; }
  .back .title .line-2 { font-size: 42px; margin-top: 2px; }
  .back .subtitle { position: absolute; left: 0; width: 548px; top: 154px; font-size: 16.5px; letter-spacing: 3.2px; line-height: 20.5px; }
  .blurb { position: absolute; left: 46px; top: 207px; width: 456px; font-family: "Gentium Book Plus", serif; font-size: 16.2px; line-height: 18.5px; hyphens: auto; -webkit-hyphens: auto; }
  .blurb p + p { margin-top: 18.5px; }

  /* Spine */
  .spine { position: absolute; left: 564px; top: 0; width: 64px; height: 834px; }
  .spine .spine-title { position: absolute; left: 12px; top: 70px; writing-mode: vertical-rl; font-family: "Montserrat", sans-serif; font-weight: 900; font-size: 37px; line-height: 1; text-transform: uppercase; white-space: nowrap; }
  .spine .spine-author { position: absolute; left: 20px; top: 556px; writing-mode: vertical-rl; font-family: "Gentium Book Plus", serif; font-size: 22px; letter-spacing: 1px; text-transform: uppercase; white-space: nowrap; }

  /* Front cover */
  .front { position: absolute; left: 628px; top: 0; width: 572px; height: 834px; }
  .front-art {
    position: absolute; left: 0; top: 0; width: 572px; height: 834px;
    background: radial-gradient(ellipse 360px 520px at 300px 400px, var(--flame-hot) 0%, var(--flame) 30%, var(--flame-red) 60%, rgba(60,16,6,.6) 85%, transparent 100%);
  }
  .front .title { position: absolute; left: 10px; width: 572px; top: 76px; }
  .front .title .line-1 { font-size: 86px; }
  .front .title .line-2 { font-size: 51px; margin-top: 4px; }
  .front .subtitle { position: absolute; left: 10px; width: 572px; top: 206px; font-size: 25.5px; line-height: 31px; letter-spacing: .5px; }
  .front-author { position: absolute; left: 10px; width: 572px; top: 762px; text-align: center; font-family: "Gentium Book Plus", serif; font-size: 34px; line-height: 1; letter-spacing: 3.5px; text-transform: uppercase; }
</style>
</head>
<body>
<main class="cover">
  <section class="back">
    <h2 class="title"><span class="line-1">Marea</span><span class="line-2">Silenciosa</span></h2>
    <p class="subtitle">Los ecos que nadie<br>quiso escuchar</p>
    <div class="blurb">
      <p>Oficina del consenso, desinformación, “fake news”... en los últimos años nos hemos visto envueltos en una discusión pública rodeados de estos términos sin terminar de entender exactamente qué significan y lo que es peor, sin saber que realmente nos rodean desde que el hombre es hombre.</p>
      <p>En esta obra el autor busca acercanos al mundo de la Marea Silenciosa, aquellas operaciones que buscan influir sobre el comportamiento de la población. Sin hacer uso de un lenguaje excesivamente técnico relata como la evolución de la naturaleza de la guerra a los parámetros del siglo XXI promueve un enfoque del conflicto que no supone un uso de la fuerza tradicional. ¿Para qué atacar las instituciones de un país de forma directa, cuando puedes fomentar el conflicto social entre grupos antagónicos y desestabilizar sin realizar un solo disparo?</p>
      <p>¿Cómo razona el ser humano? ¿Son nuestras ideas tan nuestras como creemos? ¿Por qué importa tanto el uso preciso del lenguaje a la hora de comunicarnos?, ¿Cómo nos afectan las razones y emociones de los demás? ¿Por qué tendemos a prestar mayor atención a argumentos que encajen con nuestras propias ideas? ¿Cómo nos afecta la conversación en redes sociales?</p>
      <p>Armados con el conocimiento que reside en este libro, quizás, seamos menos susceptibles de caer bajo la influencia de grupos con intereses espurios.</p>
    </div>
  </section>

  <section class="spine">
    <p class="spine-title">Marea Silenciosa</p>
    <p class="spine-author">Tomás Herreruela</p>
  </section>

  <section class="front">
    <div class="front-art" role="img" aria-label="Photograph of a distressed man holding his head in his hands, with a fiery explosion cloud rising from his head against a dark red sky"></div>
    <h1 class="title"><span class="line-1">Marea</span><span class="line-2">Silenciosa</span></h1>
    <p class="subtitle">Los ecos que nadie<br>quiso escuchar</p>
    <p class="front-author">Tomás Herreruela</p>
  </section>
</main>
</body>
</html>
```